Redesign Website for Tandara Flame

I have an existing website on https://www.tandaraflame-example.com.au/ and would like to have this redesigned professionally with new content (please refer to word document). We are fire protection engineers providing fire services design expertise and engineering design to a range of different clients.

We also provide drafting services to clients in the form of completing final commissioning documentation such as 'as-installed' drawings and fire services block plans to ensure compliance with the building code and relevant Australian Standards.

Target Market(s)

Builders, Architects, Consultants, Project Managers

Industry/Entity Type

Engineering Consultant

Coding

Coded - Design and coding required

Number of Pages Required

4 page

Font styles to use
Sans Serif

Requirements
Must have
• Home and about Page, fire services design page, fire block plans page, contact us page (4 Pages).

The website colour choice must match or compliment the new company logo.
Nice to have
• Quality photos of fire services installations in buildings to Australian Standards.

A website similar to this would be ideal http://corbellpyro-example.com.au
Should not have
• Stolen licensed photos

```html
<!DOCTYPE html>
<html lang="en">
<head>
<meta charset="utf-8">
<title>Tandara Flame — Fire Services Drawings & Block Plans</title>
<link rel="stylesheet" href="https://fonts.googleapis.com/css2?family=Jost:wght@400;500;600;700&display=swap">
<style>
:root{
  --orange:#f7931e;
  --orange-deep:#e57d0c;
  --ink:#1c1c1c;
  --text:#555;
  --muted:#888;
  --mist:#eef0f6;
  --peach:#fbe6cc;
  --beige:#f4ece2;
  --slate:#8e8e8e;
  --white:#fff;
  --footer:#f5f6f8;
}
*{box-sizing:border-box;margin:0;padding:0}
html,body{width:1200px;height:4640px;overflow:hidden}
body{font-family:"Jost",sans-serif;color:var(--ink);background:var(--white);position:relative}
.abs{position:absolute}
/* header */
.site-header{position:absolute;top:0;left:0;width:1200px;height:97px;background:var(--white);border-top:4px solid var(--orange);z-index:5}
.brand{position:absolute;left:60px;top:28px;display:flex;align-items:center;gap:10px;font-size:24px;font-weight:600;color:var(--orange)}
.brand-dot{width:26px;height:26px;border-radius:50%;background:var(--orange)}
.main-nav{position:absolute;right:48px;top:26px;display:flex;align-items:center;gap:40px;font-size:21px;color:#333}
.main-nav .cta{background:var(--orange);color:var(--white);padding:8px 34px;border-radius:24px}
.nav-caret{position:absolute;left:523px;top:93px;width:0;height:0;border-left:10px solid transparent;border-right:10px solid transparent;border-top:10px solid var(--white)}
/* hero */
.hero{position:absolute;top:97px;left:0;width:1200px;height:700px;overflow:hidden}
.hero-photo{position:absolute;inset:0;background:radial-gradient(ellipse at 70% 40%,#5c6770 0%,#2a323c 40%,#151b24 70%),#151b24}
.hero-flames{position:absolute;left:0;right:0;bottom:0;height:300px;background:linear-gradient(180deg,rgba(0,0,0,0),rgba(190,80,20,.55) 60%,rgba(230,110,30,.6))}
.hero h1{position:absolute;left:155px;top:140px;color:var(--white);font-weight:600;font-size:62px;letter-spacing:1px;line-height:1}
.hero h2{position:absolute;left:155px;top:218px;color:var(--white);font-weight:600;font-size:48px;line-height:1}
.hero p{position:absolute;left:155px;top:300px;color:var(--white);font-size:24px;line-height:36px;width:480px}
.hero .btn-light{position:absolute;left:153px;top:422px;width:182px;height:48px;background:var(--white);color:var(--ink);font-weight:600;font-size:16px;display:flex;align-items:center;justify-content:center;clip-path:polygon(8% 0,100% 0,92% 100%,0 100%);border-radius:4px}
.hero-arrow{position:absolute;top:245px;width:46px;height:46px;border:2px solid rgba(255,255,255,.8);border-radius:50%}
.hero-arrow svg{position:absolute;inset:0}
.hero-dots{position:absolute;top:563px;left:565px;display:flex;gap:8px;align-items:center}
.hero-dots i{width:14px;height:14px;border-radius:50%;background:var(--white);display:block}
.hero-dots i.on{width:18px;height:18px;background:var(--orange);border:3px solid var(--white)}
.hero-curve{position:absolute;left:0;top:600px;width:1200px;height:220px;z-index:2}
/* about */
.stat-hex{position:absolute;width:220px;height:200px}
.stat-hex svg{position:absolute;inset:0;filter:drop-shadow(0 4px 10px rgba(0,0,0,.07))}
.stat-body{position:absolute;inset:0;display:flex;flex-direction:column;align-items:center;justify-content:center;padding-top:6px}
.stat-icon{width:34px;height:40px;margin-bottom:10px}
.stat-num{font-size:26px;font-weight:500}
.stat-label{font-size:14px;color:var(--muted);margin-top:4px}
.about-title{position:absolute;left:654px;top:918px;font-size:44px;font-weight:500}
.about-copy{position:absolute;left:654px;top:985px;width:370px;font-size:14px;line-height:24px;color:var(--text)}
/* services */
.services{position:absolute;top:1290px;left:0;width:1200px;height:872px;background:var(--mist);clip-path:polygon(0 0,100% 110px,100% 100%,0 100%)}
.services-badge{position:absolute;left:570px;top:1335px;width:60px;height:60px}
.eyebrow{position:absolute;left:0;width:1200px;text-align:center;font-size:22px}
.section-title{position:absolute;left:0;width:1200px;text-align:center;font-size:42px;font-weight:400}
.section-title b{font-weight:600}
.service-card{position:absolute;width:297px;height:167px;background:var(--white);border-radius:4px;box-shadow:0 6px 14px rgba(0,0,0,.08);overflow:hidden}
.service-card h3{position:absolute;left:28px;top:52px;width:230px;font-size:18px;font-weight:500;line-height:26px}
.service-card .corner{position:absolute;right:0;bottom:0;width:110px;height:80px;background:var(--peach);clip-path:polygon(40% 0,100% 0,100% 100%,0 100%)}
.service-card .icon{position:absolute;right:18px;bottom:14px;width:54px;height:54px}
.service-card.active{background:var(--orange);color:var(--white)}
.service-card.active .corner{background:rgba(255,255,255,.18)}
.btn-pill{position:absolute;left:501px;top:2018px;width:198px;height:51px;border-radius:26px;background:var(--slate);color:var(--white);font-size:17px;display:flex;align-items:center;justify-content:center}
.notch{position:absolute;left:570px;top:2160px;border-left:30px solid transparent;border-right:30px solid transparent;border-top:32px solid var(--mist)}
/* drawings */
.drawing{position:absolute;top:2400px;width:263px;height:234px;border:1px solid #ddd;box-shadow:0 8px 16px rgba(0,0,0,.12);background:linear-gradient(135deg,#f4f4f4,#e3e6ee 45%,#d9dbe6 60%,#f2f2f2)}
.btn-outline{position:absolute;top:2663px;width:155px;height:40px;border:2px solid var(--orange);border-radius:20px;font-size:15px;display:flex;align-items:center;justify-content:center;color:#333}
/* plans */
.plans{position:absolute;top:2790px;left:0;width:1200px;height:950px;overflow:hidden}
.plans-bg{position:absolute;left:0;top:60px;width:1200px;height:890px;background:var(--orange)}
.plans-photo{position:absolute;right:0;top:60px;width:440px;height:890px;background:radial-gradient(ellipse at 70% 30%,rgba(255,220,170,.45),rgba(247,147,30,0) 65%)}
.plans-wave{position:absolute;left:0;top:0;width:1200px;height:120px}
.plans .eyebrow,.plans .section-title{color:var(--white)}
.plan-hex{position:absolute;width:297px;height:263px}
.plan-hex>svg.shape{position:absolute;inset:0}
.plan-body{position:absolute;inset:0;display:flex;flex-direction:column;align-items:center;justify-content:center;text-align:center;color:#333;font-weight:500;font-size:18px;line-height:24px}
.plan-icon{width:74px;height:74px;margin-bottom:16px}
.plan-hex.active .plan-body{color:var(--white)}
.chev{width:36px;height:36px;margin-top:12px}
/* reviews */
.reviews-title{position:absolute;left:0;top:3815px;width:1200px;text-align:center;font-size:44px}
.reviews-title b{font-weight:600}
.review{position:absolute;top:3910px;width:294px;height:312px;background:var(--white);border-radius:16px;box-shadow:0 8px 22px rgba(0,0,0,.08);padding:40px 38px}
.review h4{font-size:20px;font-weight:500;line-height:26px}
.review p{margin-top:26px;font-size:13px;line-height:23px;color:var(--text)}
.reviewer{position:absolute;left:42px;bottom:46px;display:flex;align-items:center;gap:14px}
.avatar{width:48px;height:48px;border-radius:50%;background:linear-gradient(160deg,#d9c2b0,#4a3a33)}
.stars{color:var(--orange);font-size:14px;letter-spacing:1px}
.reviewer span{display:block;font-size:13px;font-weight:500}
.rev-arrow{position:absolute;top:4035px;width:40px;height:30px}
/* footer */
.site-footer{position:absolute;top:4307px;left:0;width:1200px;height:252px;background:var(--footer)}
.footer-brand{position:absolute;left:140px;top:4408px;font-size:22px;font-weight:600;color:var(--orange)}
.socials{position:absolute;left:142px;top:4462px;display:flex;gap:8px}
.socials i{display:block;width:32px;height:32px;border-radius:50%;background:var(--orange)}
.f-head{position:absolute;top:4355px;font-size:17px;color:#333}
.f-list{position:absolute;top:4388px;font-size:14px;line-height:24px;color:#444}
.f-row{display:flex;gap:10px;align-items:flex-start;margin-bottom:14px;line-height:18px;font-size:13px}
.f-row svg{flex:none;margin-top:2px}
.map{position:absolute;left:785px;top:4397px;width:282px;height:108px;background:linear-gradient(135deg,#e6ecf3,#d5dfe9);border-bottom:4px solid var(--orange)}
.legal{position:absolute;top:4559px;left:0;width:1200px;height:81px;border-top:1px solid #e3e3e3;font-size:14px;color:#555}
.legal .copy{position:absolute;left:132px;top:28px}
.legal .links{position:absolute;right:96px;top:28px}
</style>
</head>
<body>

<header class="site-header">
  <div class="brand"><span class="brand-dot"></span>Tandara Flame</div>
  <nav class="main-nav">
    <span>Home</span><span>About</span><span>Fire Services</span><span>Fire Block</span><span class="cta">Contact Us</span>
  </nav>
  <span class="nav-caret"></span>
</header>

<section class="hero">
  <div class="hero-photo" role="img" aria-label="Photo of a fire sprinkler head spraying water over flames"></div>
  <div class="hero-flames"></div>
  <h1>FIRE SERVICES</h1>
  <h2>Drawings &amp; Block Plans</h2>
  <p>We pride ourselves on our prompt service and delivery of all of our projects.</p>
  <span class="btn-light">LEARN MORE</span>
  <span class="hero-arrow" style="left:60px"><svg viewBox="0 0 46 46"><path d="M26 14 L17 23 L26 32" fill="none" stroke="#fff" stroke-width="2"/></svg></span>
  <span class="hero-arrow" style="left:1089px"><svg viewBox="0 0 46 46"><path d="M20 14 L29 23 L20 32" fill="none" stroke="#fff" stroke-width="2"/></svg></span>
  <div class="hero-dots"><i></i><i class="on"></i><i></i></div>
</section>
<svg class="hero-curve" viewBox="0 0 1200 220" preserveAspectRatio="none">
  <path d="M0 55 Q560 230 1200 40 L1200 220 L0 220 Z" fill="#f7931e"/>
  <path d="M0 60 Q560 200 1200 45 L1200 220 L0 220 Z" fill="#fff"/>
  <path d="M0 60 Q580 170 1200 45 L1200 220 L0 220 Z" fill="#fff"/>
</svg>
<svg class="abs" style="left:0;top:640px;z-index:3" width="1200" height="160" viewBox="0 0 1200 160">
  <path d="M120 40 Q600 180 1120 20 Q600 150 120 40 Z" fill="#f7931e"/>
</svg>

<section class="about">
  <div class="stat-hex" style="left:196px;top:832px">
    <svg viewBox="0 0 220 200"><polygon points="55,2 165,2 218,100 165,198 55,198 2,100" fill="#fff" stroke="#eee"/></svg>
    <div class="stat-body"><svg class="stat-icon" viewBox="0 0 34 40"><circle cx="17" cy="11" r="9" fill="#f7931e"/><path d="M2 40 Q2 23 17 23 Q32 23 32 40Z" fill="#f7931e"/></svg><div class="stat-num">200 +</div><div class="stat-label">Total Clients</div></div>
  </div>
  <div class="stat-hex" style="left:376px;top:942px">
    <svg viewBox="0 0 220 200"><polygon points="55,2 165,2 218,100 165,198 55,198 2,100" fill="#fff" stroke="#eee"/></svg>
    <div class="stat-body"><svg class="stat-icon" viewBox="0 0 34 40"><circle cx="17" cy="11" r="9" fill="#f7931e"/><path d="M2 40 Q2 23 17 23 Q32 23 32 40Z" fill="#f7931e"/></svg><div class="stat-num">200 +</div><div class="stat-label">Total Clients</div></div>
  </div>
  <div class="stat-hex" style="left:193px;top:1045px">
    <svg viewBox="0 0 220 200"><polygon points="55,2 165,2 218,100 165,198 55,198 2,100" fill="#fff" stroke="#eee"/></svg>
    <div class="stat-body"><svg class="stat-icon" viewBox="0 0 34 40"><circle cx="17" cy="11" r="9" fill="#f7931e"/><path d="M2 40 Q2 23 17 23 Q32 23 32 40Z" fill="#f7931e"/></svg><div class="stat-num">200 +</div><div class="stat-label">Total Clients</div></div>
  </div>
  <h2 class="about-title">About the Service</h2>
  <p class="about-copy">Brindle Software is a mobile-first, Field Service Management &amp; CRM Software for Contractors and Home Improvement Professionals. Our software helps commercial and residential HVAC, plumbing, electrical, and other field service businesses, to send Estimates, Invoices, collect payments, manage clients and jobs from their mobile devices.</p>
</section>

<section class="services"></section>
<svg class="services-badge" viewBox="0 0 60 60"><polygon points="15,4 45,4 58,30 45,56 15,56 2,30" fill="#fff" stroke="#f7931e" stroke-width="3"/><circle cx="30" cy="32" r="8" fill="#f7931e"/></svg>
<div class="eyebrow" style="top:1452px;color:var(--orange)">Our Services</div>
<h2 class="section-title" style="top:1488px">Fire <b>Services Drawings</b></h2>

<div class="service-card" style="left:132px;top:1604px"><h3>Automatic Smoke Detection and Alarm System</h3><span class="corner"></span>
  <svg class="icon" viewBox="0 0 54 54" fill="none" stroke="#f7931e" stroke-width="2"><path d="M8 20 H46 Q46 36 27 36 Q8 36 8 20Z"/><circle cx="27" cy="26" r="4"/><path d="M27 40 V48"/></svg></div>
<div class="service-card active" style="left:450px;top:1604px"><h3>Emergency Warning and Intercom System</h3><span class="corner"></span>
  <svg class="icon" viewBox="0 0 54 54" fill="none" stroke="#fff" stroke-width="2"><path d="M15 40 V26 Q15 14 27 14 Q39 14 39 26 V40Z"/><path d="M11 44 H43"/><path d="M27 6 V10 M8 14 L12 17 M46 14 L42 17"/></svg></div>
<div class="service-card" style="left:771px;top:1604px"><h3>Occupant Warning System</h3><span class="corner"></span>
  <svg class="icon" viewBox="0 0 54 54" fill="none" stroke="#f7931e" stroke-width="2"><path d="M27 6 L50 46 H4Z"/><path d="M27 20 V34 M27 38 V41"/></svg></div>
<div class="service-card" style="left:132px;top:1793px"><h3>Smoke Alarms</h3><span class="corner"></span>
  <svg class="icon" viewBox="0 0 54 54" fill="none" stroke="#f7931e" stroke-width="2"><path d="M6 14 H42 Q42 24 24 24 Q6 24 6 14Z"/><path d="M44 48 Q36 40 44 30 Q52 40 44 48Z"/></svg></div>
<div class="service-card" style="left:450px;top:1793px"><h3>Fire Hose Reels</h3><span class="corner"></span>
  <svg class="icon" viewBox="0 0 54 54" fill="none" stroke="#f7931e" stroke-width="2"><circle cx="27" cy="24" r="18"/><circle cx="27" cy="24" r="10"/><circle cx="27" cy="24" r="3"/><path d="M20 42 V50 H34 V42"/></svg></div>
<div class="service-card" style="left:771px;top:1793px"><h3>Portable Fire Extinguishers</h3><span class="corner"></span>
  <svg class="icon" viewBox="0 0 54 54" fill="none" stroke="#f7931e" stroke-width="2"><rect x="16" y="18" width="20" height="32" rx="4"/><path d="M22 18 V10 H30 V18 M30 12 H42"/></svg></div>
<span class="btn-pill">View all Services</span>
<span class="notch"></span>

<div class="eyebrow" style="top:2254px;color:var(--ink)">Our Services</div>
<h2 class="section-title" style="top:2290px">Fire <b>Services Drawings</b></h2>
<div class="drawing" style="left:148px" role="img" aria-label="Sample fire services floor plan drawing"></div>
<div class="drawing" style="left:468px" role="img" aria-label="Sample fire services floor plan drawing"></div>
<div class="drawing" style="left:787px" role="img" aria-label="Sample fire services floor plan drawing"></div>
<span class="btn-outline" style="left:202px">Learn More</span>
<span class="btn-outline" style="left:522px">Learn More</span>
<span class="btn-outline" style="left:841px">Learn More</span>

<section class="plans">
  <svg class="plans-wave" viewBox="0 0 1200 120" preserveAspectRatio="none">
    <path d="M0 50 C250 20 420 8 600 30 C820 58 1000 60 1200 20 L1200 120 L0 120Z" fill="#d9730a"/>
    <path d="M0 60 C250 30 420 18 600 42 C820 70 1000 70 1200 30 L1200 120 L0 120Z" fill="#f7931e"/>
  </svg>
  <div class="plans-bg"></div>
  <div class="plans-photo" role="img" aria-label="Faded photo of a sprinkler head and flames"></div>
  <div class="eyebrow" style="top:152px">Our Plans</div>
  <h2 class="section-title" style="top:188px">Fire <b>Block Plans</b></h2>

  <div class="plan-hex" style="left:132px;top:291px">
    <svg class="shape" viewBox="0 0 297 263"><polygon points="74,0 223,0 297,131 223,263 74,263 0,131" fill="#f4ece2"/></svg>
    <div class="plan-body"><svg class="plan-icon" viewBox="0 0 74 74" fill="none" stroke="#666" stroke-width="2"><path d="M14 14 H60 M30 14 V24 H44 V14 M37 24 V32"/><path d="M37 38 V46 M24 36 L18 48 M50 36 L56 48 M30 52 L28 62 M44 52 L46 62"/></svg>Zone Block Plans
      <svg class="chev" viewBox="0 0 36 36" fill="none" stroke="#333" stroke-width="1.6"><circle cx="18" cy="18" r="16"/><path d="M11 15 L18 22 L25 15"/></svg></div>
  </div>
  <div class="plan-hex active" style="left:452px;top:291px">
    <svg class="shape" viewBox="0 0 297 263"><polygon points="74,0 223,0 297,131 223,263 74,263 0,131" fill="#8e8e8e"/></svg>
    <div class="plan-body"><svg class="plan-icon" viewBox="0 0 74 74" fill="none" stroke="#fff" stroke-width="3"><path d="M10 28 H22 L38 14 V60 L22 46 H10Z"/><path d="M48 26 Q54 37 48 48 M56 18 Q66 37 56 56"/></svg>EWIS/SSISEP<br>Block Plans
      <svg class="chev" viewBox="0 0 36 36" fill="none" stroke="#fff" stroke-width="1.6"><circle cx="18" cy="18" r="16"/><path d="M11 15 L18 22 L25 15"/></svg></div>
  </div>
  <div class="plan-hex" style="left:771px;top:291px">
    <svg class="shape" viewBox="0 0 297 263"><polygon points="74,0 223,0 297,131 223,263 74,263 0,131" fill="#f4ece2"/></svg>
    <div class="plan-body"><svg class="plan-icon" viewBox="0 0 74 74" fill="none" stroke="#666" stroke-width="2"><path d="M16 12 H58 M30 12 V22 H44 V12 M37 22 V30"/><path d="M24 36 L18 44 M50 36 L56 44 M37 36 V42"/><path d="M37 62 Q30 54 37 46 Q44 54 37 62Z"/></svg>Sprinkler Block Plans
      <svg class="chev" viewBox="0 0 36 36" fill="none" stroke="#333" stroke-width="1.6"><circle cx="18" cy="18" r="16"/><path d="M11 15 L18 22 L25 15"/></svg></div>
  </div>
  <div class="plan-hex" style="left:292px;top:574px">
    <svg class="shape" viewBox="0 0 297 263"><polygon points="74,0 223,0 297,131 223,263 74,263 0,131" fill="#f4ece2"/></svg>
    <div class="plan-body"><svg class="plan-icon" viewBox="0 0 74 74" fill="none" stroke="#666" stroke-width="2"><rect x="20" y="10" width="22" height="12"/><rect x="14" y="22" width="34" height="40"/><circle cx="31" cy="42" r="8"/><path d="M48 42 H66"/></svg>Fire Hydrant Block Plans
      <svg class="chev" viewBox="0 0 36 36" fill="none" stroke="#333" stroke-width="1.6"><circle cx="18" cy="18" r="16"/><path d="M11 15 L18 22 L25 15"/></svg></div>
  </div>
  <div class="plan-hex" style="left:611px;top:574px">
    <svg class="shape" viewBox="0 0 297 263"><polygon points="74,0 223,0 297,131 223,263 74,263 0,131" fill="#f4ece2"/></svg>
    <div class="plan-body"><svg class="plan-icon" viewBox="0 0 74 74" fill="none" stroke="#666" stroke-width="2"><path d="M14 62 H62"/><path d="M30 58 V40 L38 30 L46 40 V58 M24 44 L38 30"/><path d="M56 26 Q50 18 56 10 Q62 18 56 26Z"/></svg>Evacuation Management<br>Plan / Diagrams
      <svg class="chev" viewBox="0 0 36 36" fill="none" stroke="#333" stroke-width="1.6"><circle cx="18" cy="18" r="16"/><path d="M11 15 L18 22 L25 15"/></svg></div>
  </div>
</section>

<h2 class="reviews-title">Client <b>Reviews</b></h2>
<svg class="rev-arrow" style="left:68px" viewBox="0 0 40 30" fill="none" stroke="#555" stroke-width="2"><path d="M36 15 H6 M16 5 L6 15 L16 25"/></svg>
<svg class="rev-arrow" style="left:1092px" viewBox="0 0 40 30" fill="none" stroke="#2b6fd6" stroke-width="2"><path d="M4 15 H34 M24 5 L34 15 L24 25"/></svg>
<article class="review" style="left:132px"><h4>Lorem Ipsum is simply dummy text of the</h4><p>Lorem Ipsum is simply dummy text of the printing and typesetting industry. Lorem Ipsum has been the industry's</p>
  <div class="reviewer"><span class="avatar" role="img" aria-label="Reviewer portrait"></span><div><div class="stars">★★★★★</div><span>JANA PELLOW</span></div></div></article>
<article class="review" style="left:452px"><h4>Lorem Ipsum is simply dummy text of the</h4><p>Lorem Ipsum is simply dummy text of the printing and typesetting industry. Lorem Ipsum has been the industry's</p>
  <div class="reviewer"><span class="avatar" role="img" aria-label="Reviewer portrait"></span><div><div class="stars">★★★★★</div><span>JANA PELLOW</span></div></div></article>
<article class="review" style="left:773px"><h4>Lorem Ipsum is simply dummy text of the</h4><p>Lorem Ipsum is simply dummy text of the printing and typesetting industry. Lorem Ipsum has been the industry's</p>
  <div class="reviewer"><span class="avatar" role="img" aria-label="Reviewer portrait"></span><div><div class="stars">★★★★★</div><span>JANA PELLOW</span></div></div></article>

<footer class="site-footer"></footer>
<div class="footer-brand">Tandara Flame</div>
<div class="socials"><i></i><i></i><i></i><i></i></div>
<div class="f-head" style="left:353px">CONTACT US</div>
<div class="f-list" style="left:353px;width:200px">
  <div class="f-row"><svg width="12" height="16" viewBox="0 0 12 16"><path d="M6 16 C6 16 0 9 0 6 A6 6 0 0 1 12 6 C12 9 6 16 6 16Z" fill="#555"/><circle cx="6" cy="6" r="2" fill="#fff"/></svg><span>42 Carrow Lane Suite 3<br>Perth WA 6000</span></div>
  <div class="f-row"><svg width="14" height="14" viewBox="0 0 14 14"><path d="M3 1 L5 4 L4 6 Q6 9 8 10 L10 9 L13 11 L12 13 Q5 13 1 3Z" fill="#555"/></svg><span>(08) 5550 1742</span></div>
  <div class="f-row"><svg width="14" height="11" viewBox="0 0 14 11"><rect x="0.5" y="0.5" width="13" height="10" fill="none" stroke="#555"/><path d="M1 1 L7 6 L13 1" fill="none" stroke="#555"/></svg><span>hello@tandaraflame-example.com.au</span></div>
</div>
<div class="f-head" style="left:598px">COMPANY</div>
<div class="f-list" style="left:598px">Home<br>About Us<br>Fire Services<br>Fire Block<br>Contact Us</div>
<div class="f-head" style="left:782px">LOCATION</div>
<div class="map" role="img" aria-label="Map showing the office location"></div>
<div class="legal"><span class="copy">© 2021 Tandara Flame. All Rights Reserved.</span><span class="links">Privacy Policy &nbsp; | &nbsp; Terms of Use</span></div>

</body>
</html>
```